Verpackungen für kleine Imkerei
Zielgruppe
Wir sind eine kleine Imkerei aus dem Aargau (Schweiz) und stellen zusammen mit unseren glücklichen Bienen feinsten Honig her. Gerne möchten wir unseren visuelle Kommunikation nach aussen mit Hilfe eines neuen Etiketts verbessern.
Aufgabenstellung
Das Etikett muss rechteckig sein und wir auf einem runden Glas aufgeklebt. Die Maximalgrösse ist 210x45mm (beim 500g Glas) und entsprechend kleiner bei kleineren Einheiten. Wir möchten ein Grunddesign, welches adaptierbar ist auf die weiteren Sorten. (Waldhonig, Blütenhonig, cremiger Blütenhonig, Zürcher Stadthonig, Badener Stadthonig, Lenzburger Stadthonig). Barcode muss keinen eingefügt werden, nur die gesetzlichen Daten müssen auf dem Etiektt stehen. Weitere Wünsche und Anmerkungen befinden sich im pdf.
Sollten Dateien oder Bilder nachgereicht werden, bitte melden!

```html
<!DOCTYPE html>
<html lang="de">
<head>
<meta charset="utf-8">
<title>Honigglück – Etikett Blütenhonig</title>
<link href="https://fonts.googleapis.com/css2?family=Amatic+SC:wght@400;700&display=swap" rel="stylesheet">
<style>
  :root {
    --stage: #ececec;
    --label-white: #ffffff;
    --ink: #1b1b1b;
    --rose: #f0a3bd;
    --rose-band: #f4a9c0;
    --rose-soft: #fbe3ec;
    --band-text: #ffffff;
    --bee-gold: #e8b64a;
  }
  * { box-sizing: border-box; margin: 0; padding: 0; }
  html, body {
    width: 1200px; height: 800px; overflow: hidden;
    background: var(--stage);
    font-family: "Amatic SC", cursive;
  }
  .canvas {
    position: relative; width: 1200px; height: 800px;
    display: flex; align-items: center; justify-content: center;
  }
  .label {
    position: relative; width: 1120px; height: 240px;
    background: var(--label-white);
    box-shadow: 0 6px 18px rgba(0,0,0,.12);
    overflow: hidden;
  }
  .honeycomb-field {
    position: absolute; inset: 0 0 31px 0;
    background:
      radial-gradient(ellipse 260px 120px at 12% 55%, var(--rose-soft), transparent 70%),
      radial-gradient(ellipse 300px 120px at 40% 50%, var(--rose-soft), transparent 70%),
      radial-gradient(ellipse 300px 120px at 72% 45%, var(--rose-soft), transparent 70%),
      radial-gradient(ellipse 240px 120px at 95% 55%, var(--rose-soft), transparent 70%);
    opacity: .55;
  }
  .legal, .producer {
    position: absolute; top: 100px;
    font-size: 17px; line-height: 17px; font-weight: 700;
  }
  .legal { left: 24px; }
  .producer { left: 940px; }
  .legal .head, .producer .head { color: var(--ink); }
  .legal .info, .producer .info { color: var(--rose); font-weight: 400; }
  .gap { margin-top: 10px; }
  .brand {
    position: absolute; left: 0; right: 0; top: 18px;
    display: flex; flex-direction: column; align-items: center;
  }
  .bee-art {
    width: 240px; height: 26px; border-radius: 13px;
    background: linear-gradient(90deg, transparent, var(--bee-gold) 50%, transparent);
    opacity: .35;
  }
  .brand-name {
    font-size: 62px; line-height: 66px; font-weight: 700; color: var(--ink);
  }
  .variety {
    margin-top: 6px;
    font-size: 30px; line-height: 30px; font-weight: 400; color: var(--rose);
    letter-spacing: 1px;
  }
  .variety .dot { font-size: 20px; vertical-align: middle; padding: 0 4px; }
  .flower-art {
    margin-top: 4px; width: 22px; height: 22px; border-radius: 50%;
    background: radial-gradient(circle, var(--label-white) 25%, var(--rose) 30%, var(--rose-soft) 80%);
  }
  .weight-band {
    position: absolute; left: 0; right: 0; bottom: 0; height: 31px;
    background: var(--rose-band);
    color: var(--band-text);
    font-size: 19px; font-weight: 700; line-height: 31px; text-align: center;
  }
</style>
</head>
<body>
<main class="canvas">
  <section class="label">
    <div class="honeycomb-field" role="img" aria-label="Zartes rosa Wabenmuster im Hintergrund"></div>

    <div class="legal">
      <p class="head">Schweizer Blütenhonig</p>
      <p class="info">Honig gut verschlossen, kühl (bei max. 15°)</p>
      <p class="info">dunkel &amp; trocken lagern</p>
      <p class="head gap">Mindestens haltbar bis <span class="info">August 2022</span></p>
      <p class="info gap">Warenlos Nr. 01092018</p>
    </div>

    <div class="brand">
      <div class="bee-art" role="img" aria-label="Illustration fliegender Bienen"></div>
      <h1 class="brand-name">Honigglück</h1>
      <p class="variety"><span class="dot">•</span>Blütenhonig<span class="dot">•</span></p>
      <div class="flower-art" role="img" aria-label="Kleine Blüten-Verzierung"></div>
    </div>

    <div class="producer">
      <p class="head">Ursula &amp; Beat Karrigo</p>
      <p class="info">Lindenweg 4</p>
      <p class="info">5600 Musterdorf</p>
      <p class="head gap">Web</p>
      <p class="info">www.honigglueck.ch</p>
    </div>

    <div class="weight-band">500g Nettogewicht</div>
  </section>
</main>
</body>
</html>
```